regPersonal Trainer Flyer Design

Reason: I have been very busy with other work and would like to extend the deadline to offer designers the chance to edit and improve designs with my help. Thank you for all the designs that have been sent so far.

```html
<!DOCTYPE html>
<html lang="en">
<head>
<meta charset="utf-8">
<title>Personal Trainer Flyer – Introductory Offer</title>
<link rel="stylesheet" href="https://fonts.googleapis.com/css2?family=Oswald:wght@500;600&family=Questrial&display=swap">
<style>
  :root{
    --page:#d9dcdf;
    --card-frame:#eef0f2;
    --card-edge:#c9cdd1;
    --panel:#050505;
    --brand-blue:#0b6fbe;
    --brand-blue-dark:#084f88;
    --text-light:#ffffff;
    --text-soft:#e9ecef;
    --photo-light:#8d8d8d;
    --photo-dark:#1d1d1d;
  }
  *{box-sizing:border-box;margin:0;padding:0}
  html,body{width:1200px;height:928px;overflow:hidden;background:var(--page)}
  .flyer{
    position:absolute;left:40px;top:79px;width:1120px;height:770px;
    background:var(--card-frame);border:1px solid var(--card-edge);
  }
  .flyer-panel{
    position:absolute;left:26px;top:26px;width:1068px;height:718px;
    background:var(--panel);
  }
  .hero-photo{
    position:absolute;left:433px;top:0;width:635px;height:380px;
    background:
      linear-gradient(90deg,var(--panel) 0%,rgba(5,5,5,0) 30%),
      linear-gradient(0deg,var(--panel) 0%,rgba(5,5,5,0) 35%),
      linear-gradient(135deg,#a9a9a9 0%,var(--photo-light) 40%,#4a4a4a 75%,var(--photo-dark) 100%);
  }
  .offer-banner{position:absolute;left:-34px;top:20px;width:760px;height:170px}
  .offer-title{
    position:absolute;left:50px;top:30px;
    font-family:'Oswald',sans-serif;font-weight:600;color:var(--text-light);
    line-height:1;text-transform:uppercase;
  }
  .offer-title .line-one{display:block;font-size:58px;letter-spacing:.5px}
  .offer-title .line-two{display:block;font-size:75px;margin-top:4px}
  .benefit-list{
    position:absolute;left:50px;top:238px;width:480px;list-style:none;
    font-family:'Questrial',sans-serif;font-size:27px;color:var(--text-soft);
  }
  .benefit-list li{
    position:relative;padding-left:46px;padding-bottom:14px;margin-bottom:12px;
  }
  .benefit-list li::before{
    content:"";position:absolute;left:0;top:10px;width:17px;height:17px;border-radius:50%;
    background:radial-gradient(circle at 35% 35%,#9fd3ff 0%,var(--brand-blue) 45%,#03335a 100%);
  }
  .benefit-list li::after{
    content:"";position:absolute;left:40px;bottom:0;width:320px;height:2px;
    background:linear-gradient(90deg,rgba(255,255,255,0),rgba(255,255,255,.7) 50%,rgba(255,255,255,0));
  }
  .benefit-list li.wide::after{width:400px}
  .benefit-list li.plain::after{display:none}
  .benefit-list li.plain{line-height:1.25}
  .session-photo{
    position:absolute;border:4px solid var(--text-light);
    background:linear-gradient(160deg,#d9d9d9 0%,#a8a8a8 55%,#6e6e6e 100%);
  }
  .session-photo.pads{left:741px;top:343px;width:300px;height:180px}
  .session-photo.barbell{left:528px;top:460px;width:306px;height:200px}
  .trainer-tag{position:absolute;left:705px;top:522px;width:390px;height:172px}
  .trainer-details{
    position:absolute;right:26px;top:540px;text-align:right;
    font-family:'Oswald',sans-serif;font-weight:500;color:var(--text-light);line-height:1.2;
  }
  .trainer-name,.trainer-role{font-size:31px}
  .trainer-phone,.trainer-email{font-size:22px}
  .trainer-phone{margin-top:6px}
</style>
</head>
<body>
  <div class="flyer">
    <div class="flyer-panel">
      <div class="hero-photo" role="img" aria-label="Photo of the personal trainer doing a barbell exercise in a gym beside a punch bag"></div>

      <svg class="offer-banner" viewBox="0 0 760 170" aria-hidden="true">
        <polygon points="0,0 600,0 760,170 0,170" fill="var(--brand-blue)"/>
        <polygon points="0,170 34,170 34,186" fill="var(--brand-blue-dark)"/>
      </svg>
      <h1 class="offer-title">
        <span class="line-one">Introductory Offer</span>
        <span class="line-two">One Free Session</span>
      </h1>

      <ul class="benefit-list">
        <li>Lacking motivation?</li>
        <li class="wide">Not achieving your goals?</li>
        <li class="wide">Need help?</li>
        <li class="wide">Bored of the gym?</li>
        <li>You're never too old</li>
        <li class="wide">Training can be at your home</li>
        <li class="plain">I can help improve your health<br>and well-being</li>
      </ul>

      <div class="session-photo pads" role="img" aria-label="Photo of the trainer holding boxing pads for a client"></div>
      <div class="session-photo barbell" role="img" aria-label="Photo of the trainer coaching a client through a barbell squat"></div>

      <svg class="trainer-tag" viewBox="0 0 390 172" aria-hidden="true">
        <polygon points="90,0 390,0 390,172 0,172" fill="var(--brand-blue)"/>
      </svg>
      <div class="trainer-details">
        <p class="trainer-name">Sam Carter</p>
        <p class="trainer-role">Personal Trainer</p>
        <p class="trainer-phone">07700 900482</p>
        <p class="trainer-email">sam.carter@fitmail.co.uk</p>
      </div>
    </div>
  </div>
</body>
</html>
```